Retail Seafood business needs package/label design

In need of packaging/label design for multiple seafood products such as sword fish, halibut, cod fish, scallops, mahi, catfish, and lobster tails

```html
<!DOCTYPE html>
<html lang="en">
<head>
<meta charset="UTF-8">
<title>Lobster Tails Label</title>
<link href="https://fonts.googleapis.com/css2?family=Bodoni+Moda:wght@400;500&family=Josefin+Sans:wght@600&family=Great+Vibes&family=Arimo&display=swap" rel="stylesheet">
<style>
  :root {
    --backdrop: #52687a;
    --paper: #f2f3f3;
    --navy: #144a72;
    --ink: #1c1f24;
    --brand-text: #e9e4d8;
    --sketch: #d6dde4;
    --sketch-deep: #b9c8d6;
  }
  * { margin: 0; padding: 0; box-sizing: border-box; }
  html, body {
    width: 1200px;
    height: 800px;
    overflow: hidden;
    background: var(--backdrop);
  }
  .canvas {
    position: relative;
    width: 1200px;
    height: 800px;
  }
  .label {
    position: absolute;
    left: 344px;
    top: 33px;
    width: 512px;
    height: 734px;
    background: var(--paper);
    overflow: hidden;
  }
  .brand-band {
    position: absolute;
    left: 0;
    top: 38px;
    width: 100%;
    height: 125px;
    background: var(--navy);
    display: flex;
    align-items: center;
    justify-content: center;
    gap: 10px;
  }
  .brand-name {
    font-family: "Josefin Sans", sans-serif;
    font-weight: 600;
    font-size: 28px;
    letter-spacing: 2px;
    color: var(--brand-text);
    text-transform: uppercase;
  }
  .brand-dot {
    width: 10px;
    height: 10px;
    border-radius: 50%;
    background: var(--brand-text);
  }
  .sketch-backdrop {
    position: absolute;
    left: 0;
    top: 170px;
    width: 240px;
    height: 564px;
    background: linear-gradient(180deg, rgba(214,221,228,0.0) 0%, rgba(214,221,228,0.55) 40%, rgba(214,221,228,0.25) 100%);
  }
  .lobster-art {
    position: absolute;
    left: 250px;
    top: 208px;
    width: 262px;
    height: 305px;
    background: radial-gradient(ellipse at 55% 45%, var(--sketch-deep) 0%, var(--sketch) 55%, rgba(214,221,228,0) 80%);
  }
  .product-title {
    position: absolute;
    left: 38px;
    top: 262px;
    font-family: "Bodoni Moda", serif;
    font-weight: 400;
    font-size: 60px;
    line-height: 64px;
    color: var(--ink);
    letter-spacing: -1px;
  }
  .origin {
    position: absolute;
    left: 38px;
    top: 420px;
    font-family: "Bodoni Moda", serif;
    font-size: 38px;
    color: var(--navy);
    letter-spacing: -0.5px;
  }
  .claims {
    position: absolute;
    left: 80px;
    top: 550px;
    display: flex;
    gap: 34px;
  }
  .claim {
    font-family: "Great Vibes", cursive;
    font-size: 30px;
    line-height: 32px;
    color: var(--ink);
    text-align: center;
  }
  .net-weight {
    position: absolute;
    left: 0;
    top: 652px;
    width: 100%;
    display: flex;
    align-items: center;
    gap: 30px;
  }
  .net-weight .rule {
    flex: 1;
    height: 6px;
    background: var(--navy);
  }
  .net-weight .amount {
    font-family: "Arimo", sans-serif;
    font-size: 27px;
    color: var(--ink);
  }
</style>
</head>
<body>
<div class="canvas">
  <section class="label">
    <header class="brand-band">
      <span class="brand-name">Tidewell Groceries</span>
      <span class="brand-dot"></span>
    </header>

    <div class="sketch-backdrop" role="img" aria-label="Faint line sketch of seafood in the background"></div>
    <div class="lobster-art" role="img" aria-label="Navy line illustration of a lobster"></div>

    <h1 class="product-title">lobster<br>tails</h1>
    <p class="origin">honduras</p>

    <div class="claims">
      <p class="claim">100%<br>Fresh</p>
      <p class="claim">Premium<br>Quality</p>
      <p class="claim">Hand Cut<br>Seafood</p>
    </div>

    <div class="net-weight">
      <span class="rule"></span>
      <span class="amount">5 oz</span>
      <span class="rule"></span>
    </div>
  </section>
</div>
</body>
</html>
```